Property Report

8 page document, similar theme to our website (www.harbourandvale.example) and previous brochure (provided). All content provided. We want a professional looking document. We need ASAP. Thanks!

Industry/Entity Type

Property

Font styles to use
Serif
Sans Serif

Colors
ffc214
ffcf3e
fee18a
fff3d1

Requirements
Must have
• Page 1: Cover
Page 2: Content
Page 3: About Us
Page 4: Site Description
Page 5: Scheme
Page 6: Analysis
Page 7: Conclusion
Page 8: Contact Details

```html
<!DOCTYPE html>
<html lang="en">
<head>
<meta charset="utf-8">
<title>Site Report – Harbour &amp; Vale Commercial</title>
<link href="https://fonts.googleapis.com/css2?family=Outfit:wght@300;400;500&display=swap" rel="stylesheet">
<style>
:root{
  --backdrop:#d6d7db;
  --charcoal:#5f6062;
  --charcoal-dark:#3e3f41;
  --gold:#ffc214;
  --gold-soft:#ffcf3e;
  --gold-pale:#fee18a;
  --cream:#fff3d1;
  --ink:#1e1e1e;
  --muted:#5a5a5a;
  --white:#ffffff;
}
*{box-sizing:border-box;margin:0;padding:0}
html,body{width:951px;height:1200px;overflow:hidden;background:var(--backdrop)}
body{font-family:"Outfit",sans-serif;color:var(--ink)}
.canvas{position:relative;width:951px;height:1200px}
.page{position:absolute;width:272px;height:352px;overflow:hidden}
.photo{position:absolute}
.pg-cover{left:33px;top:31px}
.pg-contents{left:338px;top:31px}
.pg-about{left:643px;top:31px}
.pg-site{left:33px;top:424px}
.pg-scheme{left:338px;top:424px}
.pg-cases{left:642px;top:424px}
.pg-valuation{left:36px;top:815px}
.pg-conclusion{left:339px;top:815px}
.pg-contact{left:642px;top:815px}

.wordmark{position:absolute;left:0;right:0;text-align:center;color:var(--white);font-weight:500;line-height:1.05}
.wordmark .wm-main{font-size:20px;display:block}
.wordmark .wm-sub{font-size:9px;display:block;margin-top:2px}

.heading{position:absolute;font-weight:400;font-size:16px;line-height:1}
.heading-rule{position:absolute;height:0;border-top:0.6px solid var(--ink)}
.body-copy{position:absolute;font-size:4.6px;line-height:1.5;font-weight:300}
.body-copy p+p{margin-top:5px}

/* cover */
.cover-title{position:absolute;top:270px;left:0;right:0;text-align:center;color:var(--white);font-size:14px;font-weight:300;letter-spacing:.3px}
.cover-rule{position:absolute;top:292px;left:41px;width:192px;border-top:0.7px solid var(--gold)}
.cover-address{position:absolute;top:304px;left:0;right:0;text-align:center;color:var(--white);font-size:7px}
.cover-behalf{position:absolute;top:317px;left:0;right:0;text-align:center;color:var(--white);font-size:5px;font-weight:300}
.cover-client{position:absolute;top:325px;left:0;right:0;text-align:center;color:var(--white);font-size:6.2px;font-style:italic}

/* contents */
.contents-box{position:absolute;left:123px;top:177px;width:149px;height:145px;background:rgba(255,194,20,.85)}
.contents-list{position:absolute;left:0;top:45px;width:110px;list-style:none;font-size:5.6px}
.contents-list li{display:flex;justify-content:flex-end;align-items:center;height:12px}
.contents-list .dash{width:8px;border-top:0.6px solid var(--ink);margin:0 5px}
.contents-list .num{width:7px;font-weight:500}

/* site description */
.dark-copy{color:#e9e9e9}

/* scheme */
.scheme-box{position:absolute;left:123px;top:105px;width:149px;height:140px;background:rgba(255,194,20,.88)}

/* case studies */
.cases-head{position:absolute;left:0;top:0;width:272px;height:53px;background:linear-gradient(100deg,#606164 60%,#8d8f93)}
.case-band{position:absolute;left:0;width:272px;height:100px}
.case-band.b1{top:53px;background:var(--cream)}
.case-band.b2{top:153px;background:var(--gold-pale)}
.case-band.b3{top:253px;height:99px;background:linear-gradient(120deg,var(--gold-soft),var(--gold))}
.case-img{position:absolute;width:94px;height:81px;top:9px}
.case-text{position:absolute;top:20px;width:120px;font-size:4.3px;line-height:1.5;font-weight:300}
.case-text h3{font-size:7px;font-weight:400;margin-bottom:6px;letter-spacing:.2px}
.case-text p+p{margin-top:5px}

/* valuation */
.val-note{position:absolute;left:36px;top:106px;width:200px;height:17px;border:0.7px solid var(--gold);color:var(--white);font-size:4.6px;display:flex;align-items:center;justify-content:center;font-weight:300}
.val-table{position:absolute;left:13px;top:146px;width:246px;border-collapse:collapse;background:var(--white);table-layout:fixed}
.val-table th{height:25px;background:linear-gradient(180deg,#fedb7a,var(--gold-pale));font-size:7px;font-weight:400;text-align:right;vertical-align:bottom;padding:0 4px 2px 0}
.val-table th.corner{width:39px}
.val-table td{height:14px;font-size:3.6px;text-align:center;border-top:0.5px solid #fff}
.val-table td.rate{font-size:7px;text-align:left;padding-left:3px}
.val-table tr:nth-child(even) td{background:#e4e4e6}
.val-table tr:nth-child(odd) td{background:#f3f3f3}
.val-table td.hl{background:#fbe3a0 !important}

/* conclusion */
.conclusion-copy ul{list-style:none;padding-left:7px}
.conclusion-copy li::before{content:"— ";}
.conclusion-copy p{margin-top:4px}

/* contact */
.contact-name{position:absolute;top:264px;left:0;right:0;text-align:center;color:var(--white);font-size:10.5px}
.contact-addr{position:absolute;top:279px;left:0;right:0;text-align:center;color:var(--white);font-size:6px;font-weight:300}
.contact-rule{position:absolute;top:292px;left:42px;width:188px;border-top:0.7px solid var(--gold)}
.contact-phone{position:absolute;top:300px;left:0;right:0;text-align:center;color:var(--white);font-size:7.5px}
.contact-web{position:absolute;top:312px;left:0;right:0;text-align:center;color:var(--white);font-size:5.4px;font-weight:300}
</style>
</head>
<body>
<main class="canvas">

  <!-- Cover -->
  <section class="page pg-cover">
    <div class="photo" role="img" aria-label="Black and white photo of three business people silhouetted against a city skyline window" style="inset:0;background:linear-gradient(180deg,#4a4a4c 0%,#8a8b8d 30%,#6c6d6f 55%,#3d3e40 100%)"></div>
    <div class="wordmark" style="top:40px"><span class="wm-main">Harbour &amp; Vale</span><span class="wm-sub">Commercial</span></div>
    <h1 class="cover-title">SITE REPORT</h1>
    <div class="cover-rule"></div>
    <p class="cover-address">118 Ashcombe Road, Westbury KT9 2QP</p>
    <p class="cover-behalf">On behalf of</p>
    <p class="cover-client">NORWOOD LANE GROUP LIMITED</p>
  </section>

  <!-- Contents -->
  <section class="page pg-contents">
    <div class="photo" role="img" aria-label="Black and white photo of an office block behind a bare tree" style="inset:0;background:linear-gradient(160deg,#8d8d8d 0%,#5a5a5a 45%,#3a3a3a 75%,#6d6d6d 100%)"></div>
    <div class="contents-box">
      <h2 class="heading" style="left:38px;top:18px">Contents</h2>
      <div class="heading-rule" style="left:0;top:38px;width:149px"></div>
      <ul class="contents-list">
        <li>About Us<span class="dash"></span><span class="num">03</span></li>
        <li>Site Description<span class="dash"></span><span class="num">04</span></li>
        <li>Scheme<span class="dash"></span><span class="num">05</span></li>
        <li>Case Studies<span class="dash"></span><span class="num">06</span></li>
        <li>Analysis<span class="dash"></span><span class="num">07</span></li>
        <li>Conclusion<span class="dash"></span><span class="num">08</span></li>
        <li>Contact Details<span class="dash"></span><span class="num">09</span></li>
      </ul>
    </div>
  </section>

  <!-- About Us -->
  <section class="page pg-about" style="background:var(--cream)">
    <div class="photo" role="img" aria-label="Photo of a white corner pub building under blue sky" style="left:0;top:0;width:272px;height:177px;background:linear-gradient(180deg,#2f6fc2 0%,#7fa8dc 35%,#d9d4c6 60%,#8a5a45 85%,#7d7d7d 100%)"></div>
    <h2 class="heading" style="left:25px;top:195px">About Us</h2>
    <div class="heading-rule" style="left:0;top:214px;width:98px"></div>
    <div class="body-copy" style="left:79px;top:230px;width:162px">
      <p>Harbour &amp; Vale Commercial specialise in the acquisition and disposal of development, investment and commercial property in London and the Home Counties. Our consultants advise on a wide range of property types and use classes and are experts in identifying ways in which property owners can maximise value.</p>
      <p>Our considerable knowledge of the property market and creative approach to delivering maximum value, has enabled us to become one of the most active development and investment consultancies in London and the South East.</p>
    </div>
  </section>

  <!-- Site Description -->
  <section class="page pg-site" style="background:var(--charcoal)">
    <h2 class="heading" style="left:27px;top:34px;color:var(--white)">Site Description</h2>
    <div class="heading-rule" style="left:0;top:53px;width:150px;border-color:var(--gold)"></div>
    <div class="body-copy dark-copy" style="left:64px;top:63px;width:175px">
      <p>Harbour and Vale Commercial have been asked by Daniel Norwood the representative for Norwood Lane Group Limited to advise on the best disposal method to maximise value for their property.</p>
      <p>The existing property measures approximately 9,655 square feet internally with parking spaces.</p>
      <p>The site was granted permitted development rights in 2016 to be converted into 11 flats and 11 parking spaces but this was no implemented.</p>
      <p>We understand that the vendors operate their business from the premises and the property has a designated use class of B1(a) Office/E Class.</p>
    </div>
    <div class="photo" role="img" aria-label="Street photo of office buildings along a city road" style="left:0;top:177px;width:272px;height:175px;background:linear-gradient(180deg,#c7d8ec 0%,#9aa6b3 30%,#6b5b4e 65%,#4c4c4e 100%)"></div>
  </section>

  <!-- Scheme -->
  <section class="page pg-scheme">
    <div class="photo" role="img" aria-label="Photo of a person using a tablet at a white desk" style="left:0;top:0;width:272px;height:176px;background:linear-gradient(135deg,#e9eaec 0%,#c8c9cc 50%,#8e8f93 100%)"></div>
    <div class="photo" role="img" aria-label="Photo of a glass facade in pale blue tones" style="left:0;top:176px;width:272px;height:176px;background:linear-gradient(120deg,#b8d4de 0%,#e6f0f3 50%,#a7c4cf 100%)"></div>
    <div class="scheme-box">
      <h2 class="heading" style="left:19px;top:39px">Scheme</h2>
      <div class="heading-rule" style="left:0;top:59px;width:149px"></div>
      <div class="body-copy" style="left:37px;top:73px;width:80px;font-size:4.8px">
        <p>We have taken advice form Linework Architects who have reviewed the site and have come up with a scheme for 30 residential units</p>
      </div>
    </div>
  </section>

  <!-- Case Studies -->
  <section class="page pg-cases">
    <div class="cases-head">
      <h2 class="heading" style="left:41px;top:14px;color:var(--white)">Case Studies</h2>
      <div class="heading-rule" style="left:0;top:32px;width:150px;border-color:var(--gold)"></div>
      <p style="position:absolute;left:87px;top:36px;width:62px;text-align:right;color:#f0f0f0;font-size:7.5px;font-weight:300">Comparables</p>
    </div>
    <div class="case-band b1">
      <div class="photo case-img" role="img" aria-label="Photo of a tower under construction beside a road" style="left:15px;background:linear-gradient(180deg,#dfe6ee 0%,#b7bcc2 50%,#6c6f73 100%)"></div>
      <div class="case-text" style="left:126px">
        <h3>ELMFIELD HOUSING GROUP -</h3>
        <p>Maple Clinic, Ferris Road, Westbury<br>KT9 3AB</p>
        <p>37 residential Units<br>Price - £4,486,970 Per plot £121,000<br>August 2019</p>
      </div>
    </div>
    <div class="case-band b2">
      <div class="case-text" style="left:30px;width:125px">
        <h3>PRIVATE DEVELOPER -</h3>
        <p>Car Sales Show Rooms And Lock Ups Adjacent To Arterial Service Station, Carver Road, Holmdale, London SW40 1ZZ</p>
        <p>32 Residential Flats<br>Price £1,400,000 - Per Plot £44,000<br>August 2019</p>
      </div>
      <div class="photo case-img" role="img" aria-label="Aerial photo of a street with flats and parked cars" style="left:163px;background:linear-gradient(180deg,#c9d9ea 0%,#a1a4a8 45%,#8b6a58 100%)"></div>
    </div>
    <div class="case-band b3">
      <div class="photo case-img" role="img" aria-label="Photo of a new brick apartment block by a road" style="left:15px;background:linear-gradient(180deg,#cfdcea 0%,#a5644e 55%,#6e6e70 100%)"></div>
      <div class="case-text" style="left:126px">
        <h3>BRIGHTWATER HOUSING -</h3>
        <p>Land On The South Side Of Penrose Road,<br>London SW41 7DD</p>
        <p>74 Residential Flats<br>Price - £11,050,000 Per Plot £149,000<br>June 2017</p>
      </div>
    </div>
  </section>

  <!-- Valuation -->
  <section class="page pg-valuation" style="background:var(--charcoal)">
    <h2 class="heading" style="left:90px;top:44px;color:var(--white)">Valuation</h2>
    <div class="heading-rule" style="left:0;top:63px;width:166px;border-color:var(--gold)"></div>
    <p style="position:absolute;left:33px;top:67px;color:#f0f0f0;font-size:8px;font-weight:300">Consented Site Valuation Variable</p>
    <div class="val-note">Please see below assumed land valuation upon delivery of planning permission.</div>
    <table class="val-table">
      <tr><th class="corner"></th><th>30</th><th>32</th><th>34</th><th>36</th><th>38</th><th>40</th><th>42</th></tr>
      <tr><td class="rate">£ 65,000</td><td>£ 1,950,000</td><td>£ 2,080,000</td><td>£ 2,210,000</td><td>£ 2,340,000</td><td>£ 2,470,000</td><td>£ 2,600,000</td><td>£ 2,730,000</td></tr>
      <tr><td class="rate">£ 75,000</td><td>£ 2,250,000</td><td>£ 2,400,000</td><td class="hl">£ 2,550,000</td><td>£ 2,700,000</td><td>£ 2,850,000</td><td>£ 3,000,000</td><td>£ 3,150,000</td></tr>
      <tr><td class="rate">£ 85,000</td><td>£ 2,550,000</td><td>£ 2,720,000</td><td class="hl">£ 2,890,000</td><td class="hl">£ 3,060,000</td><td class="hl">£ 3,230,000</td><td>£ 3,400,000</td><td>£ 3,400,000</td></tr>
      <tr><td class="rate">£ 95,000</td><td>£ 2,850,000</td><td>£ 3,040,000</td><td>£ 3,230,000</td><td>£ 3,420,000</td><td>£ 3,610,000</td><td>£ 3,800,000</td><td>£ 3,800,000</td></tr>
      <tr><td class="rate">£105,000</td><td>£ 3,150,000</td><td>£ 3,360,000</td><td>£ 3,570,000</td><td>£ 3,780,000</td><td>£ 3,990,000</td><td>£ 4,200,000</td><td>£ 4,200,000</td></tr>
    </table>
  </section>

  <!-- Conclusion -->
  <section class="page pg-conclusion" style="background:var(--cream)">
    <div class="photo" role="img" aria-label="Photo of a brick parade of shops with flats above" style="left:0;top:0;width:272px;height:176px;background:linear-gradient(180deg,#dde3ea 0%,#8a5a48 35%,#6d4a3e 65%,#4e4f55 85%,#8c8d90 100%)"></div>
    <h2 class="heading" style="left:18px;top:196px">Conclusion</h2>
    <div class="heading-rule" style="left:0;top:215px;width:104px"></div>
    <div class="body-copy conclusion-copy" style="left:42px;top:226px;width:210px;font-size:4.4px;line-height:1.35">
      <p>Package Led Land Sale Involves selling the site to a Housing Association with a contractor already in place.</p>
      <p>Benefits:</p>
      <ul>
        <li>Housing Association has build cost certainty.</li>
        <li>No need to tender build.</li>
        <li>More interest from HA if builder in place.</li>
        <li>HA responds better to contractor.</li>
        <li>Contractor will identify potential issues coming from HA.</li>
        <li>No SDLT or CIL.</li>
      </ul>
      <p>Private Sale</p>
      <ul><li>Likely to be of interest to private market but beholden to market conditions and market appetite.</li></ul>
      <p>Alternative User</p>
      <ul><li>Limited Experience in Private Rented Sector and income led purchasers as is a relatively new market.</li></ul>
    </div>
  </section>

  <!-- Contact -->
  <section class="page pg-contact">
    <div class="photo" role="img" aria-label="Black and white aerial photo of a city along a river" style="inset:0;background:linear-gradient(150deg,#5c5c5e 0%,#3f4042 45%,#6a6b6d 70%,#3a3b3d 100%)"></div>
    <div class="wordmark" style="top:162px"><span class="wm-main">Harbour &amp; Vale</span><span class="wm-sub">Commercial</span></div>
    <p class="contact-name">Harbour &amp; Vale Commercial</p>
    <p class="contact-addr">Unit 4 Marlow Yard London SE40 9QT</p>
    <div class="contact-rule"></div>
    <p class="contact-phone">020 7946 0321</p>
    <p class="contact-web">info@harbourandvale.example &nbsp;|&nbsp; www.harbourandvale.example</p>
  </section>

</main>
</body>
</html>
```